Business Card for Wellness Clinic

We need a business card for our new logo. I want it to match the feel of the logo

Target Market(s)

Young professional families looking for holistic health care

Industry/Entity Type

Health And Wellness

Contact Information for Business Card

Our business Name: Larkvale Health & wellness Centre, our phone #, email address...see attached old business card

Font styles to use
Sans Serif

Colors
33b8a4
cee9f5

Requirements
Must have
• my logo and business name
• Font is "Helvetica Neue LT Std 45 Light" and
• Only for "&" using font "Trajan pro bold"
• Use colors in the logo

```html
<!DOCTYPE html>
<html lang="en">
<head>
<meta charset="utf-8">
<title>Larkvale Health &amp; Wellness Centre – Business Cards</title>
<link rel="stylesheet" href="https://fonts.googleapis.com/css2?family=Roboto:wght@300;400&display=swap">
<style>
  :root {
    --teal: #2db5a1;
    --grey-text: #9a9a9a;
    --grey-band: #b0b0b0;
    --rule: #c8c8c8;
    --card: #ffffff;
    --backdrop: #ececec;
  }
  * { margin: 0; padding: 0; box-sizing: border-box; }
  html, body { width: 1189px; height: 1200px; overflow: hidden; }
  body {
    background: var(--backdrop);
    font-family: "Roboto", "Helvetica Neue", Arial, sans-serif;
    font-weight: 300;
    position: relative;
  }
  .card {
    position: absolute;
    left: 171px;
    width: 856px;
    height: 488px;
    background: var(--card);
    overflow: hidden;
  }
  .card--front { top: 67px; }
  .card--back { top: 626px; }
  .card > * { position: absolute; }

  .brand-mark { width: 96px; height: 96px; background: var(--teal); border-radius: 10px; }
  .brand-name { color: var(--teal); font-weight: 300; white-space: nowrap; line-height: 1; }
  .brand-name__top { display: block; font-size: 30px; letter-spacing: 0.2em; }
  .brand-name__bottom { display: block; font-size: 18px; letter-spacing: 0.58em; margin-top: 18px; }

  .card--front .brand-mark { left: 210px; top: 44px; }
  .card--front .brand-name { left: 38px; top: 174px; }

  .doctor { right: 36px; top: 262px; text-align: right; }
  .doctor__name { color: var(--teal); font-size: 29px; font-weight: 300; line-height: 1.2; }
  .doctor__title { color: var(--grey-text); font-size: 21px; line-height: 1.3; }

  .divider { left: 38px; top: 329px; width: 782px; height: 1px; background: var(--rule); }

  .address { left: 38px; top: 352px; color: var(--grey-text); font-size: 21px; line-height: 30px; font-style: normal; }
  .online { right: 36px; top: 376px; color: var(--grey-text); font-size: 21px; line-height: 32px; text-align: right; }

  .front-bands { left: 0; bottom: 0; width: 856px; height: 33px; }

  .card--back .brand-mark { left: 380px; top: 44px; }
  .card--back .brand-name { left: 205px; top: 170px; }

  .field-label { color: var(--teal); font-size: 23px; }
  .field-line { height: 1px; background: #8c8c8c; }
  .label-date { left: 54px; top: 281px; }
  .line-date { left: 130px; top: 305px; width: 283px; }
  .label-time { left: 427px; top: 281px; }
  .line-time { left: 512px; top: 305px; width: 284px; }
  .label-for { left: 92px; top: 326px; }
  .line-for { left: 153px; top: 350px; width: 608px; }

  .policy { left: 0; width: 100%; top: 371px; text-align: center; color: var(--grey-text); font-size: 20px; line-height: 29px; }

  .footer-band {
    left: 0; bottom: 0; width: 100%; height: 49px;
    background: var(--teal); color: #fff; font-size: 22px;
    display: flex; align-items: center; justify-content: center;
  }
</style>
</head>
<body>

<section class="card card--front" aria-label="Business card front">
  <div class="brand-mark" aria-hidden="true"></div>
  <p class="brand-name">
    <span class="brand-name__top">LARKVALE HEALTH &amp;</span>
    <span class="brand-name__bottom">WELLNESS CENTRE</span>
  </p>

  <div class="doctor">
    <p class="doctor__name">DR. MAREN HOLT, N.D.</p>
    <p class="doctor__title">Naturopathic Doctor</p>
  </div>

  <div class="divider"></div>

  <address class="address">
    48 Fenwick Ave, Suite 305<br>
    Brookfield, ON K1A 2B7<br>
    613-555-0147
  </address>

  <p class="online">
    mholt@larkvalenaturopathic.ca<br>
    www.larkvalenaturopathic.ca
  </p>

  <svg class="front-bands" viewBox="0 0 856 33" aria-hidden="true">
    <polygon points="0,10 530,10 521,33 0,33" fill="var(--grey-band)"/>
    <polygon points="543,0 856,0 856,33 530,33" fill="var(--teal)"/>
  </svg>
</section>

<section class="card card--back" aria-label="Appointment card back">
  <div class="brand-mark" aria-hidden="true"></div>
  <p class="brand-name">
    <span class="brand-name__top">LARKVALE HEALTH &amp;</span>
    <span class="brand-name__bottom">WELLNESS CENTRE</span>
  </p>

  <span class="field-label label-date">Date :</span>
  <span class="field-line line-date"></span>
  <span class="field-label label-time">Time :</span>
  <span class="field-line line-time"></span>
  <span class="field-label label-for">For :</span>
  <span class="field-line line-for"></span>

  <p class="policy">
    If you are unable to keep your appointment, please provide at least<br>
    2 business days notice or full visit fees will apply.
  </p>

  <div class="footer-band">www.larkvalenaturopathic.ca</div>
</section>

</body>
</html>
```